Contest - label design for a health related product with 4 color variations

Nuvera-Store (http://www.nuvera-store.example) is an online shop selling health related products and nutritional supplements, such as algae products, wheat grass and barley grass powder. These products have a positive impact on a person's health. Through Craft Huddle, we have designed already a logo for the shop and now we need to create labels that will be placed on a brown glass bottle (see attachment). The logo shall be used without the slogan 'One life. Live it healthy.' when creating the label.

Your job is to design a label with 4 color variations, blue, green, red and yellow. The measurements of the label is 80 mm x 173 mm, but please add 3 mm bleed to each side.

The information that has to go on the label can be taken from the attachment 'label information.pdf'. For the sake of communication, we will divide the label into 3 parts

- left
- middle
- right

The left part and the right part are fixed as this contains legal information. Please use easy to read fonts, non-serifed fonts, such as Arial, Verdana, Calibri. The left part contains a table and if Illustrator provides the possibility for tables, please use it as we need to be able to easily add and remove rows of the table.

The middle part contains the product description, the product quantity (i.e. 100 g), our logo without the slogan 'One live. Live it healthy.' and logos indicating the organic quality of the product (please see attachments). For the product name (i.e. QUB-Tangen) and the quantity (i.e. 100 Tabletten, 200 g) use the attached Lato font. Please note that the vertical position of our logo, the product name and the organic logos has NOT been set yet. You are free to position them where ever you feel in the middle part of the label.

Target Market(s)

Health concious people between 25 and 70

Industry/Entity Type

Health

Requirements
Must have
• - the attached logo without the slogan "One life...."
- the following attributes: healthy, joyful, vivid, lively, abstract, minimalistic
- colors that go along with our logo and the website www.nuvera-store.example
- all fonts need to be editable and not rendered
- the left part should have an editable table where we can add rows if necessary
- the attached font for product name and quantity
- 3 mm bleed on each side, so the final design is 6 mm wider and higher
- the final design will be in editable Illustrator files of a recent version.
Should not have
• - many overlaying, confusing lines or layers
- dark colors
- heavy appearance

```html
<!DOCTYPE html>
<html lang="de">
<head>
<meta charset="utf-8">
<title>QUB-Tangen – Etikett</title>
<link rel="stylesheet" href="https://fonts.googleapis.com/css2?family=Lato:wght@300;400&family=Arimo:wght@400;700&display=swap">
<style>
  :root {
    --paper: #ffffff;
    --white: #ffffff;
    --badge-green: #6fb33f;
  }
  /* colour variants of the label: blue, green, red, yellow */
  .label--blue   { --field-light: #48c4ef; --field: #1ba8e0; --field-mid: #2996cf; --band: #2e3b78; --ink: #2c3869; }
  .label--green  { --field-light: #8fd46a; --field: #5bb640; --field-mid: #46a033; --band: #24603a; --ink: #1f4a2c; }
  .label--red    { --field-light: #f58a7a; --field: #e5533f; --field-mid: #cf3f30; --band: #7a2230; --ink: #5a1a24; }
  .label--yellow { --field-light: #ffe07a; --field: #f7c531; --field-mid: #eab01c; --band: #8a5a12; --ink: #5c3d0c; }

  * { box-sizing: border-box; margin: 0; padding: 0; }
  html, body {
    width: 1200px; height: 568px; overflow: hidden;
    background: var(--paper);
  }
  .label {
    position: relative;
    width: 1200px; height: 568px;
    font-family: "Arimo", Arial, sans-serif;
    color: var(--ink);
  }
  .label-bg { position: absolute; left: 0; top: 0; }
  .panel {
    position: absolute;
    font-size: 11.8px;
    line-height: 14.3px;
  }
  .panel-left { left: 25px; top: 131px; width: 250px; }
  .panel-right { left: 909px; top: 131px; width: 258px; }
  .block { margin-bottom: 14.3px; }
  .block-title { font-weight: 700; }
  .notes { list-style: none; }
  .notes li { padding-left: 9px; text-indent: -9px; }
  .product {
    position: absolute; left: 305px; width: 588px; text-align: center;
    font-family: "Lato", sans-serif; color: var(--ink);
  }
  .product-name { top: 276px; font-size: 55px; font-weight: 400; letter-spacing: 0.3px; line-height: 1; }
  .product-quantity { top: 350px; font-size: 20px; font-weight: 300; }
  .shop-mark {
    position: absolute; left: 345px; top: 478px;
    display: flex; align-items: center; gap: 9px;
    font-family: "Arimo", Arial, sans-serif; font-size: 18px; color: var(--white);
  }
  .shop-mark-dot { width: 16px; height: 16px; border-radius: 50%; background: var(--white); }
  .badges { position: absolute; left: 739px; top: 468px; display: flex; gap: 8px; }
  .badge { width: 60px; height: 48px; }
  .badge-organic-de { background: var(--white); border-radius: 8px; }
  .badge-organic-eu { width: 68px; background: var(--badge-green); }
</style>
</head>
<body>
<div class="label label--blue">
  <svg class="label-bg" width="1200" height="568" viewBox="0 0 1200 568" aria-hidden="true">
    <defs>
      <radialGradient id="fieldGlow" cx="0.5" cy="0.42" r="0.62">
        <stop offset="0" style="stop-color: var(--field-light)"/>
        <stop offset="0.55" style="stop-color: var(--field)"/>
        <stop offset="1" style="stop-color: var(--field-mid)"/>
      </radialGradient>
    </defs>
    <rect x="12" y="12" width="1176" height="544" fill="url(#fieldGlow)"/>
    <path d="M12 12 H1188 V42 C1000 70 700 108 500 100 C300 92 150 80 12 74 Z" style="fill: var(--band)"/>
    <path d="M12 74 C150 80 300 92 500 100 C700 108 1000 70 1188 42 V54 C1000 86 700 122 500 116 C300 108 150 94 12 88 Z" style="fill: var(--field-mid)" opacity="0.6"/>
    <path d="M12 462 C250 446 450 436 650 438 C850 440 1050 428 1188 404 V556 H12 Z" style="fill: var(--field-mid)" opacity="0.55"/>
    <path d="M12 492 C250 474 450 462 650 462 C850 462 1050 448 1188 424 V556 H12 Z" style="fill: var(--band)" opacity="0.85"/>
    <line x1="305" y1="100" x2="305" y2="440" stroke="#ffffff" stroke-opacity="0.25"/>
    <line x1="893" y1="80" x2="893" y2="430" stroke="#ffffff" stroke-opacity="0.25"/>
  </svg>

  <section class="panel panel-left">
    <div class="block">
      <p class="block-title">Zutaten</p>
      <p>QUB-Tangen (AFA-Aphanizonenon Flos Aqua) aus dem Klamath Lake, bei 37° Celsius getrocknet.</p>
    </div>
    <div class="block">
      <p class="block-title">Nährwertangaben in 100 g pro Kapsel</p>
      <p>Kohlenhydrate</p><p>Fett</p><p>Eiweiß</p><p>Brennwert (kJ / kcal)</p>
    </div>
    <div class="block">
      <p class="block-title">Inhaltsstoffe</p>
      <p>Vitamin C (<b>pro Kapsel</b> 50,2 mg), (<b>%RDA</b> 50 %)</p>
    </div>
    <div class="block">
      <p class="block-title">Vertrieb</p>
      <p>Merrow Vale Limited</p><p>Lindenhofgasse 14</p><p>1140 Wien</p><p>Österreich</p>
    </div>
  </section>

  <h1 class="product product-name">QUB-Tangen</h1>
  <p class="product product-quantity">100 Tabletten, 200 g</p>

  <section class="panel panel-right">
    <div class="block">
      <p class="block-title">Verzehrempfehlung</p>
      <p>3 x täglich 3 – 5 Tabletten unzerkaut mit Wasser zu den Mahlzeiten einnehmen.</p>
    </div>
    <div class="block">
      <p class="block-title">Hinweise</p>
      <ul class="notes">
        <li>- Die angegebene tägliche Verzehrmenge sollte nicht überschritten werden.</li>
        <li>- Nahrungsergänzungsmittel sind kein Ersatz für eine ausgewogene und abwechslungsreiche Ernährung.</li>
        <li>- Das Produkt lichtgeschützt, verschlossen und außerhalb der Reichweite von kleinen Kindern aufbewahren.</li>
        <li>- Während der Schwangerschaft und Stillzeiten sollte vor dem Verzehr von Nahrungsergänzungsmitteln ein Arzt konsultiert werden.</li>
      </ul>
    </div>
    <div class="block">
      <p class="block-title">Mindesthaltbarkeitsdatum</p>
      <p>Siehe Boden.</p>
    </div>
  </section>

  <div class="shop-mark"><span class="shop-mark-dot"></span><span>Nuvera-Store</span></div>

  <div class="badges">
    <div class="badge badge-organic-de" role="img" aria-label="Bio-Siegel"></div>
    <div class="badge badge-organic-eu" role="img" aria-label="EU-Bio-Siegel"></div>
  </div>
</div>
</body>
</html>
```